VoltNest EV Charger Installation

We are an electrical contractor "Brannock Electric" http://brannockelectricworks.example.

New site is for a division we are creating. http://voltnestelectric.example/ is registered on Google domains.
Company is registered as VoltNest LLC.
VoltNest is something we are trying out to see if we can find a niche installing EV chargers and EV Charger outlets in existing homes and businesses. Looking to work it as a division off from Brannock Electric short term and if successful it would become a stand alone business. Often times this requires additional work to meet code. Work such as adding smoke & carbon monoxide detectors, new electrical panels and upgrading the electrical Main Service Meter system.
Will need to coordinate this site with our current Brannock Electric website. Not sure how this can work. We like the look of our current Brannock Electric Wordpress site, but it is dated and broken, in need of a rebuild or repair as well.
Need a website as a landing point for Google Maps inquiries and possibly as a way to drive customers to call for our services. Need to be mindful that we want to avoid confusion with people looking for EV charger Stations to drive and plug in their cars. We are a contractor not a place to plug in! The name may be problematic in this sense.
Looking for a site that coordinates style & color with the provided VoltNest logo. Would like to have a contact / inquiry page with a captcha or similar tool to weed out spam. need to integrate google maps and similar tools to measure marketing, assist in lead generation, etc.
Have Logo artwork. Not sure what format is best to upload.

Target Market(s)

People with electric cars, business owners and homeowners.

Industry/Entity Type

Electrical Contractor- Residential & Light Commercial (mostly residential)

Requirements
Must have
• Landing Page/about us , Contact Us/ inquiry Page with a quality captcha filter, Job Gallery- we don't have many pics yet. Google pointers /tools. Open to suggestions here! Mobile Phone/ Tablet friendly is important. I listed coded design but not quite sure what that means.
Nice to have
• Similar to the Brannock Electric site style a possibility, but open to suggestions. Possibly have something that shows the business is connected to Brannock Electric? ..."A division of Brannock Electric" with logo/link to site?

```html
<!DOCTYPE html>
<html lang="en">
<head>
<meta charset="utf-8">
<title>VoltNest EV Charger Installation</title>
<link href="https://fonts.googleapis.com/css2?family=Montserrat:wght@400;500;600;700;800&display=swap" rel="stylesheet">
<style>
:root{
  --green:#6cc24a;
  --green-dark:#4f9a31;
  --black:#0b0b0b;
  --ink:#1c1c1c;
  --grey:#e9e9e9;
  --mid:#8a8a8a;
  --white:#ffffff;
  --navy:#0e1a2b;
}
*{box-sizing:border-box;margin:0;padding:0}
html,body{width:1200px;height:3164px;overflow:hidden}
body{font-family:"Montserrat",Arial,sans-serif;color:var(--ink);background:var(--white);position:relative}
.btn{display:inline-block;font-size:13px;font-weight:700;letter-spacing:.06em;text-transform:uppercase;padding:14px 30px;text-decoration:none}
.btn-green{background:var(--green);color:var(--white)}
.btn-white{background:var(--white);color:var(--ink)}
.btn-dark{background:var(--black);color:var(--white)}

/* hero */
.hero{position:absolute;left:0;top:0;width:1200px;height:640px;overflow:hidden;
  background:linear-gradient(100deg,#050607 0%,#0c1218 38%,#1d3550 70%,#5f7c98 100%)}
.hero-photo{position:absolute;right:0;top:0;width:720px;height:640px;
  background:radial-gradient(ellipse at 60% 45%,#9fb8cf 0%,#4a6a8a 35%,rgba(12,18,24,0) 75%)}
.nav{position:absolute;left:0;top:0;width:1200px;height:90px;display:flex;align-items:center;justify-content:space-between;padding:0 110px}
.brand{display:flex;align-items:center;gap:12px;color:var(--white);font-size:30px;font-weight:800}
.brand-mark{width:26px;height:26px;background:var(--green)}
.nav-links{display:flex;gap:38px;list-style:none}
.nav-links a{color:var(--white);font-size:13px;font-weight:600;text-decoration:none;text-transform:uppercase}
.nav-links a.active{color:var(--green)}
.hero-copy{position:absolute;left:120px;top:210px;width:560px}
.hero h1{color:var(--white);font-size:44px;font-weight:800;line-height:1.12;text-transform:uppercase}
.hero h1 span{color:var(--green)}
.hero p{color:var(--white);font-size:20px;font-weight:500;line-height:1.4;margin-top:26px}
.hero-actions{display:flex;gap:20px;margin-top:44px}

/* about */
.about{position:absolute;left:0;top:640px;width:1200px;height:740px;background:var(--black);color:var(--white)}
.eyebrow{display:flex;align-items:center;gap:14px;font-size:13px;font-weight:500}
.eyebrow::before{content:"";width:10px;height:10px;background:var(--green)}
.about .rule{position:absolute;left:120px;top:70px;width:900px;height:1px;background:#333}
.about .eyebrow{position:absolute;left:120px;top:90px}
.about-intro{position:absolute;left:120px;top:160px;width:360px}
.about-intro h3{font-size:28px;font-weight:400}
.about-intro h2{font-size:32px;font-weight:700;line-height:1.2;margin-top:18px}
.about-intro p{font-size:12px;line-height:1.7;color:#cfcfcf;margin-top:26px}
.features{position:absolute;left:530px;top:290px;width:620px;display:grid;grid-template-columns:1fr 1fr;column-gap:50px;row-gap:44px}
.feature h4{font-size:15px;font-weight:700;display:flex;align-items:center;gap:12px}
.feature h4::before{content:"";width:8px;height:8px;border:2px solid var(--white);border-radius:50%}
.feature p{font-size:12px;line-height:1.65;color:#cfcfcf;margin-top:14px;padding-left:22px}
.about .cta{position:absolute;right:70px;top:640px}

/* who we are */
.who{position:absolute;left:0;top:1380px;width:1200px;height:540px;background:var(--green)}
.who-photo{position:absolute;left:0;top:0;width:420px;height:540px;background:linear-gradient(180deg,#ecebe6 0%,#d9d7cf 100%)}
.who-photo-frame{position:absolute;left:300px;top:40px;width:150px;height:460px;background:var(--white)}
.who-photo-inner{position:absolute;left:0;top:0;width:400px;height:540px;background:linear-gradient(160deg,#f1f0ec 0%,#dedcd4 60%,#c9c6bc 100%)}
.who-copy{position:absolute;left:560px;top:140px;width:560px}
.who-copy .eyebrow{font-size:24px;font-weight:400;color:var(--ink)}
.who-copy .eyebrow::before{background:var(--black);width:14px;height:14px}
.who-copy h2{font-size:34px;font-weight:700;margin-top:16px;color:var(--black)}
.who-copy p{font-size:12px;line-height:1.7;margin-top:28px;color:#1f3a14}
.who-copy .btn{position:absolute;right:0;top:320px}

/* projects */
.projects{position:absolute;left:0;top:1920px;width:1200px;height:700px;background:var(--white)}
.projects .eyebrow{position:absolute;left:120px;top:110px;color:var(--green);font-size:12px}
.projects .rule{position:absolute;left:120px;top:96px;width:900px;height:1px;background:#e2e2e2}
.projects h3{position:absolute;left:120px;top:180px;font-size:26px;font-weight:400}
.projects h2{position:absolute;left:120px;top:220px;font-size:34px;font-weight:700}
.project{position:absolute;top:300px;width:460px;height:200px}
.project.one{left:130px;top:330px}
.project.two{left:620px;top:290px}
.project-img{position:absolute;left:0;top:0;width:230px;height:180px;box-shadow:16px 16px 0 var(--ink)}
.project.one .project-img{background:linear-gradient(135deg,#f2f2f2,#b9bcc0)}
.project.two .project-img{background:linear-gradient(135deg,#eaeef0,#9ea6ad)}
.project-body{position:absolute;left:260px;top:10px;width:200px}
.project-body h5{font-size:13px;font-weight:700}
.project-body ul{list-style:none;margin-top:10px}
.project-body li{font-size:11px;line-height:1.75;color:#444;display:flex;align-items:center;gap:8px}
.project-body li::before{content:"";width:5px;height:5px;background:var(--green)}
.projects .all{position:absolute;right:130px;top:580px}
.projects .all::after{content:"";position:absolute;left:-16px;top:12px;width:100%;height:100%;background:var(--ink);z-index:-1}

/* contact */
.contact{position:absolute;left:0;top:2620px;width:1200px;height:300px;background:var(--grey)}
.contact h2{position:absolute;left:250px;top:30px;font-size:24px;font-weight:700}
.contact-info{position:absolute;left:250px;top:80px;display:flex;gap:40px;font-size:12px}
.contact-info span{display:flex;align-items:center;gap:8px}
.contact-info svg{width:14px;height:14px}
.field{position:absolute;background:var(--white);border:1px solid #d4d4d4;font-size:12px;color:var(--mid);padding:12px}
.f-name{left:250px;top:118px;width:340px;height:40px}
.f-mail{left:600px;top:118px;width:350px;height:40px}
.f-msg{left:250px;top:168px;width:700px;height:70px}
.contact .btn{position:absolute;left:750px;top:250px;padding:12px 26px}

/* footer */
.footer{position:absolute;left:0;top:2920px;width:1200px;height:244px;background:var(--white)}
.footer-brands{position:absolute;left:250px;top:30px;width:700px;display:flex;justify-content:space-between;align-items:center}
.footer-brands .name{font-size:34px;font-weight:800;color:var(--ink);display:flex;align-items:center;gap:12px}
.footer-brands .name.alt{color:#c8102e}
.socials{position:absolute;left:555px;top:170px;display:flex;gap:12px}
.socials span{width:22px;height:22px;border-radius:50%;background:#555}
.copy{position:absolute;left:0;top:208px;width:1200px;text-align:center;font-size:11px;color:var(--mid)}
</style>
</head>
<body>

<header class="hero">
  <div class="hero-photo" role="img" aria-label="Close-up of an EV charging cable plugged into a car, blue-lit"></div>
  <nav class="nav">
    <div class="brand"><span class="brand-mark"></span>VoltNest</div>
    <ul class="nav-links">
      <li><a class="active" href="#">Home</a></li>
      <li><a href="#">Contact Us</a></li>
      <li><a href="#">Our Work</a></li>
    </ul>
  </nav>
  <div class="hero-copy">
    <h1>Need an electric<br>car <span>charger?</span></h1>
    <p>Electric vehicles (EVs) are here.<br>Let VoltNest help you get powered up!</p>
    <div class="hero-actions">
      <a class="btn btn-green" href="#">About Us</a>
      <a class="btn btn-white" href="#">Contact Us</a>
    </div>
  </div>
</header>

<section class="about">
  <div class="rule"></div>
  <div class="eyebrow">EV charger installation</div>
  <div class="about-intro">
    <h3>VoltNest is</h3>
    <h2>Licensed and Insured Electrical Contractor</h2>
    <p>EV charger installation is a relatively simple process, but it's important to hire a qualified electrician. VoltNest is a division of Brannock Electric, a licensed and insured electrical contractor. We are committed to providing our customers with a quality, code-approved installation.<br><br>We'll assess your home's electrical system and help find a safe and convenient location for the charger or charger outlet.<br><br>At times older homes need a larger panel or a service upgrade to handle the added load. Additionally, some jurisdictions require smoke and carbon monoxide detectors to be brought up to current code standards. We can help you determine if any upgrades are needed and provide you with a quote for the work.</p>
  </div>
  <div class="features">
    <div class="feature"><h4>The Cost</h4><p>The cost of EV charger installation will vary depending on a number of factors, including the type of charger, the distance and access to the electrical panel. Typical charger installations range from $800 to $2,000.</p></div>
    <div class="feature"><h4>The Enjoyment</h4><p>Once your EV charger is installed, you'll start enjoying the convenience of at-home charging and the many benefits of owning an EV.</p></div>
    <div class="feature"><h4>The Permit</h4><p>VoltNest will acquire the required electrical permit for your job.</p></div>
    <div class="feature"><h4>The Discussing</h4><p>We look forward to discussing your EV charger installation evaluation and estimate.</p></div>
  </div>
  <a class="btn btn-green cta" href="#">Contact VoltNest Today</a>
</section>

<section class="who">
  <div class="who-photo-inner" role="img" aria-label="Wall-mounted EV charger with coiled cable in a garage"></div>
  <div class="who-copy">
    <div class="eyebrow">Who we are &amp; Why we are</div>
    <h2>The Best For the Job</h2>
    <p>VoltNest is a small family run business with over thirty years of experience in electrical work. We focus on installing EV chargers and EV charger outlets in existing homes and businesses. As a division of Brannock Electric, we often handle the extra work needed to meet code, such as adding detectors, new panels and upgrading the main service meter system.</p>
    <a class="btn btn-dark" href="http://brannockelectricworks.example">Go to Brannock Electric</a>
  </div>
</section>

<section class="projects">
  <div class="rule"></div>
  <div class="eyebrow">Our Vision</div>
  <h3>Our Recent</h3>
  <h2>Projects</h2>
  <article class="project one">
    <div class="project-img" role="img" aria-label="Garage wall with new electrical panels and charger outlet"></div>
    <div class="project-body">
      <h5>Lorem Ipsum</h5>
      <ul><li>Lorem ipsum dolor sit amet</li><li>Consectetur adipiscing elit</li><li>Lorem ipsum dolor sit amet</li><li>Consectetur adipiscing elit</li></ul>
    </div>
  </article>
  <article class="project two">
    <div class="project-img" role="img" aria-label="Upgraded main service meter and breaker panels on a wall"></div>
    <div class="project-body">
      <h5>Lorem Ipsum</h5>
      <ul><li>Lorem ipsum dolor sit amet</li><li>Consectetur adipiscing elit</li><li>Lorem ipsum dolor sit amet</li><li>Consectetur adipiscing elit</li></ul>
    </div>
  </article>
  <a class="btn btn-green all" href="#">View All Projects</a>
</section>

<section class="contact">
  <h2>CONTACT US</h2>
  <div class="contact-info">
    <span><svg viewBox="0 0 24 24"><path fill="#6cc24a" d="M6.6 10.8a15 15 0 0 0 6.6 6.6l2.2-2.2c.3-.3.7-.4 1-.2 1.1.4 2.3.6 3.6.6.6 0 1 .4 1 1V20c0 .6-.4 1-1 1A17 17 0 0 1 3 4c0-.6.4-1 1-1h3.5c.6 0 1 .4 1 1 0 1.3.2 2.5.6 3.6.1.3 0 .7-.2 1z"/></svg>(555) 014-2290</span>
    <span><svg viewBox="0 0 24 24"><rect x="2" y="5" width="20" height="14" fill="#6cc24a"/><path d="M2 5l10 8 10-8" fill="none" stroke="#fff" stroke-width="2"/></svg>info@voltnestelectric.example</span>
  </div>
  <div class="field f-name">Your Name</div>
  <div class="field f-mail">Email</div>
  <div class="field f-msg">Your Message</div>
  <a class="btn btn-dark" href="#">Send Your Message</a>
</section>

<footer class="footer">
  <div class="footer-brands">
    <div class="name"><span class="brand-mark"></span>VoltNest</div>
    <div class="name alt">Brannock Electric</div>
  </div>
  <div class="socials"><span></span><span></span><span></span></div>
  <div class="copy">© 2024 VoltNest LLC</div>
</footer>

</body>
</html>
```